Stationary Design - Veloria Clinic

We are looking for a stylish and professional stationary design for a facial plastic surgeon. The stationary design will be for letterhead, business card, appointment cards and envelopes.
The design must be slick and aesthetically pleasing whilst incorporating the style of our logo as attached below.

Target Market(s)

Adults of all ages

Font styles to use
Serif
Script

Requirements
Must have
• Must be an aesthetically pleasing, stylish and professional design that includes the required information in a captivating layout.
• Must also be welcoming with a balanced design and a clean crisp finish.
• Details should include:
• Mr Dorian Halvet - Consultant Otolaryngologist & Facial Plastic Surgeon
• Phone: 03 5917 2846
• Fax: 03 5918 4072
• Email: info@kmfacialplastics.example.au
• Consulting from: Bendigo, Echuca, Epping, Waverley & Melbourne CBD
• Appointment Card should include:
• Date, time, fee and location as per the attached example.
• location addresses are:
• 41 Marlow Street Echuca Vic 3564
• 318 Bramble Street Bendigo Vic 3550
• Level 3, 612 Hadley Street, Epping Vic 3076
• Level 6, 480 Tennant Street Melbourne Vic 3000
Should not have
• Clutter

```html
<!DOCTYPE html>
<html lang="en">
<head>
<meta charset="utf-8">
<title>Veloria Clinic Stationery</title>
<link href="https://fonts.googleapis.com/css2?family=Poppins:wght@300;400&display=swap" rel="stylesheet">
<style>
  :root {
    --backdrop: #dedede;
    --paper: #f7f7f7;
    --ink: #3a3a3a;
    --ink-soft: #5a5a5a;
    --rule: #9a9a9a;
    --flap: #404040;
    --flap-ink: #f0f0f0;
    --faint: #e2e2e2;
    --sig: #d6e2f2;
  }
  * { margin: 0; padding: 0; box-sizing: border-box; }
  html, body { width: 1200px; height: 877px; overflow: hidden; }
  body {
    background: var(--backdrop);
    font-family: "Poppins", sans-serif;
    color: var(--ink);
    position: relative;
  }
  .sheet {
    position: absolute;
    background: var(--paper);
    box-shadow: 0 2px 8px rgba(0,0,0,0.18);
    overflow: hidden;
  }

  .brand {
    position: absolute;
    font-weight: 400;
    color: var(--ink);
    letter-spacing: 0.16em;
    text-transform: uppercase;
    white-space: nowrap;
  }

  /* Letterhead */
  .letterhead { left: 69px; top: 64px; width: 527px; height: 742px; }
  .letterhead .brand { left: 50%; top: 84px; transform: translate(-50%, -50%); font-size: 13px; }
  .salutation { position: absolute; left: 45px; top: 206px; font-size: 13.5px; font-weight: 300; }
  .body-copy { position: absolute; left: 45px; top: 249px; width: 440px; font-size: 7.4px; line-height: 11.4px; color: var(--ink-soft); }
  .body-copy p { margin-bottom: 11.4px; text-align: justify; }
  .closing { position: absolute; left: 45px; top: 486px; font-size: 7.4px; color: var(--ink-soft); }
  .signature { position: absolute; left: 41px; top: 518px; width: 94px; height: 40px; background: var(--sig); border-radius: 3px; }
  .footer-rule { position: absolute; left: 39px; width: 456px; height: 0; border-top: 0.8px solid var(--rule); }
  .footer-rule.top { top: 674px; }
  .footer-rule.bottom { top: 707px; }
  .contact { position: absolute; font-size: 7.4px; line-height: 10.5px; color: var(--ink-soft); }
  .contact li { list-style: none; display: flex; align-items: center; gap: 4px; }
  .contact.left { left: 41px; top: 679px; }
  .contact.right { right: 32px; top: 680px; text-align: right; }
  .contact.right li { justify-content: flex-end; }
  .contact svg { width: 7px; height: 7px; fill: var(--ink); flex: none; }
  .address-line { position: absolute; left: 0; right: 0; top: 714px; font-size: 7.4px; color: var(--ink-soft); display: flex; justify-content: center; align-items: center; gap: 4px; }
  .address-line svg { width: 7px; height: 9px; fill: var(--ink); }

  /* Envelope back */
  .envelope-back { left: 614px; top: 269px; width: 531px; height: 241px; }
  .envelope-back .flap { position: absolute; left: 0; top: 0; }
  .envelope-back .brand { left: 50%; top: 39px; transform: translate(-50%, -50%); font-size: 8px; color: var(--flap-ink); }

  /* Envelope front */
  .envelope-front { left: 614px; top: 562px; width: 532px; height: 241px; }
  .envelope-front .brand { left: 32px; top: 62px; transform: translateY(-50%); font-size: 11px; }
  .envelope-front .return { position: absolute; left: 32px; top: 107px; font-size: 6.8px; color: var(--ink-soft); }
  .envelope-front .faint-name { position: absolute; right: 24px; top: 110px; font-size: 38px; font-weight: 300; color: var(--faint); letter-spacing: 0.1em; text-transform: uppercase; white-space: nowrap; }
</style>
</head>
<body>

<section class="sheet letterhead">
  <div class="brand">Veloria Clinic</div>
  <h1 class="salutation">Dear Mr. Pryce,</h1>
  <div class="body-copy">
    <p>Lorem ipsum dolor sit amet, consectetur adipiscing elit. Donec orci purus, luctus vitae dignissim eu, iaculis sed purus. Vivamus faucibus, ipsum nec aliquet viverra, leo mauris condimentum ligula, sit amet sagittis enim ligula quis arcu. Nam egestas tortor id nisi porttitor mattis. In tortor ante, ultricies in suscipit a, tempus non massa. Vivamus et auctor mi. Fusce vel massa nulla. Phasellus nec eros mauris, et scelerisque orci.</p>
    <p>Donec malesuada orci vitae nulla accumsan porta a id massa. Quisque accumsan iaculis magna sit amet fringilla. Maecenas consequat, magna eget tincidunt semper, odio nibh rutrum mi, id feugiat ante nisi eu risus. Vestibulum nunc orci, rhoncus a placerat in, ultricies in mi. Cras mattis varius eros, vel fringilla nisi suscipit eget. Quisque scelerisque sagittis nulla at porttitor.</p>
    <p>Sed id augue vitae urna euismod commodo aliquet a quam. Pellentesque arcu velit, cursus et malesuada ut, consequat et diam. Nullam erat sem, rhoncus id ullamcorper vitae, rhoncus et arcu. In ultricies ultricies nulla, ut rutrum nisi iaculis at. Donec eu magna a metus ornare faucibus. Fusce aliquet faucibus ultricies. Morbi semper, est id tincidunt gravida, sem arcu adipiscing lacus, ac bibendum nulla leo eu purus. Quisque nec diam sed risus consectetur a ccumsan quis quis nibh. Vestibulum id purus lorem.</p>
    <p>It is a long established fact that a reader will be distracted by the readable content of a page when looking at its layout. The point of using Lorem Ipsum is that it has a more-or-less normal distribution of letters, as opposed to using 'Content here, content here', making it look like readable English. Many desktop publishing packages</p>
  </div>
  <p class="closing">Sincerely,</p>
  <div class="signature" role="img" aria-label="Handwritten signature of Alan Pryce in blue ink"></div>

  <div class="footer-rule top"></div>
  <ul class="contact left">
    <li><svg viewBox="0 0 10 10"><path d="M2 0.5 L3.6 0.5 L4.3 2.8 L3.2 3.8 Q4.2 5.8 6.2 6.8 L7.2 5.7 L9.5 6.4 L9.5 8 Q9.5 9.5 8 9.5 Q0.5 9 0.5 2 Q0.5 0.5 2 0.5Z"/></svg>03 5917 2846</li>
    <li><svg viewBox="0 0 10 10"><path d="M2.5 0.5 H7.5 V3 H9.5 V8 H7.5 V9.5 H2.5 V8 H0.5 V3 H2.5Z M3.5 6 V8.5 H6.5 V6Z"/></svg>03 5918 4072</li>
  </ul>
  <ul class="contact right">
    <li>admin@harbourentclinic.example.au<svg viewBox="0 0 10 10"><path d="M0.5 2 H9.5 V8 H0.5Z M1 2.5 L5 5.5 L9 2.5" stroke="#f7f7f7" stroke-width="0.6"/></svg></li>
    <li>www.harbourentclinic.example.au<svg viewBox="0 0 10 10"><circle cx="5" cy="5" r="4.5"/><path d="M0.5 5 H9.5 M5 0.5 Q2 5 5 9.5 Q8 5 5 0.5" stroke="#f7f7f7" stroke-width="0.6" fill="none"/></svg></li>
  </ul>
  <div class="footer-rule bottom"></div>
  <p class="address-line"><svg viewBox="0 0 10 13"><path d="M5 0.5 A4.5 4.5 0 0 1 9.5 5 Q9.5 8 5 12.5 Q0.5 8 0.5 5 A4.5 4.5 0 0 1 5 0.5Z M5 3 A2 2 0 1 0 5 7 A2 2 0 1 0 5 3Z"/></svg>318 Bramble Street Bendigo</p>
</section>

<section class="sheet envelope-back">
  <svg class="flap" width="531" height="74" viewBox="0 0 531 74">
    <path d="M0 0 H531 L521 44 Q514 74 484 74 H47 Q17 74 10 44 Z" fill="var(--flap)"/>
  </svg>
  <div class="brand">Veloria Clinic</div>
</section>

<section class="sheet envelope-front">
  <div class="brand">Veloria Clinic</div>
  <p class="return">318 Bramble Street Bendigo</p>
  <p class="faint-name">Veloria</p>
</section>

</body>
</html>
```